Website for Architecture & Interior Design firm

We are architecture and interior design firm looking for website design, word press based, smooth, elegant and easy to use for visitors. It should be easy to navigate using a mobile phone, with the ability to change pictures easily. It is a Bilingual website, (English: left to right, Arabic: right to left). A button in the menu bar is required to change the language, At first, we expect an English version, then we will help the designer by providing Arabic translation for any part of the website. Our website main purpose is to display our works in a picture format (Portfolio) to our clients, which mainly consist of four galleries from our (Services) as follow: 1- Architecture 2- Interior Design 3- Project Management 4- Importing from Abroad - Each service will have its page, which displays projects(items) in thumbnail format with simple text, which deploys (when clicked) into Fullscreen gallery to show the items related pictures (Dark gray or black background). - Navigation buttons/arrows are required, (X) button to close the navigation. - This is a very important part, the user experience in PC/Browser mode or Mobile mode should be easy, error-free and fast. Our homepage consists of four main elements: A- Edge to edge picture (Changing in a smooth transitional way, Random pictures from our Services) with our Logo, also persistent menu bar in the top (Home | About Us | Architecture | Interior design | Project Management | Importing from Abroad) + Social media icons B- Photo tiles (Random pictures from our Services) C- Our Services in a fixed 4-tile picture (Clickable) D- Contact Section (Simple name, contact number, message form) We expect the final service should be: 1- a fully functioning website, WordPress based, ready to be used by visitors 2- full content filling, we will contact the designer and provide the material (texture, text,etc..)
Colors
Designer to choose colors to be used in the design.
Look and feel
Each slider illustrates characteristics of the customer's brand and the style your logo design should communicate.

```html
<!DOCTYPE html>
<html lang="en">
<head>
<meta charset="utf-8">
<title>Arcwell Studio — Architecture &amp; Interior Design</title>
<link href="https://fonts.googleapis.com/css2?family=Raleway:ital,wght@0,300;0,400;0,500;0,600;0,700;1,300;1,400&family=Playfair+Display:ital,wght@1,600&display=swap" rel="stylesheet">
<style>
:root{
  --gold:#c7a57c;
  --topbar:#2a2a2a;
  --hero:#2b2824;
  --welcome:#303030;
  --services:#2b2b2b;
  --projects:#232323;
  --contact:#2f2f2f;
  --panel:#3a3a3a;
  --field:#505050;
  --white:#ffffff;
  --ink:#222222;
  --muted:#cfcfcf;
  --grey:#777777;
}
*{margin:0;padding:0;box-sizing:border-box}
html,body{width:1200px;height:3529px;overflow:hidden}
body{font-family:'Raleway',sans-serif;background:var(--projects);color:var(--white);position:relative}
.abs{position:absolute}
.gold{color:var(--gold)}
.btn{position:absolute;background:var(--gold);color:var(--white);font-size:10px;font-weight:700;letter-spacing:.3px;display:flex;align-items:center;justify-content:center;border-radius:2px}

/* top bar */
.topbar{position:absolute;left:0;top:0;width:1200px;height:44px;background:var(--topbar);font-size:9px;color:#ddd}
.topbar .item{position:absolute;top:16px;display:flex;align-items:center;gap:7px}
.dot{width:8px;height:8px;border-radius:50%;background:#ddd;position:absolute;top:18px}

/* header */
.header{position:absolute;left:0;top:44px;width:1200px;height:89px;background:var(--white)}
.brand{position:absolute;left:166px;top:33px;font-size:14px;font-weight:600;color:#35507a;letter-spacing:.5px}
.brand-mark{display:inline-block;width:12px;height:12px;background:#35507a;margin-right:6px;vertical-align:-1px}
.nav{position:absolute;right:162px;top:37px;display:flex;gap:26px;font-size:10px;color:#333;text-transform:uppercase}
.nav .active{color:var(--gold);text-decoration:underline}

/* hero */
.hero{position:absolute;left:0;top:133px;width:1200px;height:492px;background:linear-gradient(180deg,#2f2b27,#25221f 60%,#1f1d1b)}
.hero-count{position:absolute;left:234px;top:282px;font-size:11px}
.hero-line{position:absolute;left:162px;top:288px;width:60px;height:2px;background:#ddd}
.hero-title{position:absolute;left:162px;top:305px;font-size:38px;font-weight:400;font-style:italic;line-height:45px}
.arrow-box{position:absolute;width:60px;height:60px;display:flex;align-items:center;justify-content:center}

/* welcome */
.welcome{position:absolute;left:0;top:625px;width:1200px;height:465px;background:var(--welcome)}
.h2{font-size:22px;font-weight:600}
.rule{position:absolute;height:3px;width:50px;background:var(--gold)}
.para{font-size:10.5px;line-height:22.5px;color:var(--muted)}

/* services */
.services{position:absolute;left:0;top:1090px;width:1200px;height:538px;background:var(--services)}
.card-head{position:absolute;background:var(--white);color:var(--ink);height:82px;width:210px}
.card-head .t{position:absolute;left:42px;top:25px;font-size:11px;font-weight:500}
.card-head .bar{position:absolute;left:12px;top:30px;width:22px;height:2px;background:var(--ink)}
.card-head .r{position:absolute;left:42px;top:48px;font-size:8px;text-decoration:underline;color:#555}
.card-head .n{position:absolute;right:8px;top:22px;font-size:26px;color:#eee}

/* projects */
.proj-panel{position:absolute;background:var(--white);color:var(--ink)}
.proj-panel h3{position:absolute;font-size:18px;font-weight:600}
.proj-panel .num{position:absolute;font-size:36px;color:#eee;font-weight:300}
.proj-panel .hr{position:absolute;height:1px;background:#e6e6e6}
.proj-panel p{position:absolute;font-size:10px;line-height:22.5px;color:var(--grey)}
.proj-panel .link{position:absolute;font-size:10px;font-weight:700}

/* contact */
.contact{position:absolute;left:0;top:2922px;width:1200px;height:607px;background:var(--contact)}
.form{position:absolute;left:536px;top:88px;width:501px;height:427px;background:var(--panel)}
.field{position:absolute;left:45px;width:412px;height:45px;background:var(--field);font-size:10px;font-style:italic;color:#bbb;padding:16px 15px}
</style>
</head>
<body>

<div class="topbar">
  <div class="item" style="left:162px"><svg width="11" height="11" viewBox="0 0 11 11"><rect x="2" y="1" width="7" height="9" fill="none" stroke="#c7a57c"/></svg>Building 24, Lorem Ipsum</div>
  <div class="item" style="left:308px"><svg width="14" height="10" viewBox="0 0 14 10"><rect x=".5" y=".5" width="13" height="9" fill="none" stroke="#c7a57c"/><path d="M.5 .5L7 6 13.5.5" fill="none" stroke="#c7a57c"/></svg>supportemail@example.com</div>
  <div class="item" style="left:469px"><svg width="11" height="11" viewBox="0 0 11 11"><path d="M2 1l2 2-1 2 3 3 2-1 2 2-2 1C4 10 1 7 1 3z" fill="none" stroke="#c7a57c"/></svg>+1 555 010 234</div>
  <span class="dot" style="left:916px"></span>
  <span class="dot" style="left:938px"></span>
  <span class="dot" style="left:962px"></span>
  <span class="abs" style="left:988px;top:13px;width:1px;height:16px;background:#555"></span>
  <span class="abs" style="left:1005px;top:19px;width:8px;height:6px;background:#c0c0c0"></span>
  <span class="abs" style="left:1017px;top:16px;font-size:8px">EN ▾</span>
</div>

<header class="header">
  <div class="brand"><span class="brand-mark"></span>Arcwell Studio</div>
  <nav class="nav">
    <span class="active">Home</span><span>About</span><span>Architecture</span><span>Interior Design</span><span>Project Managment</span><span>Import From Abroad</span><span>Contact Us</span>
  </nav>
</header>

<section class="hero" role="img" aria-label="Dim living room interior with sofa and metal side table">
</section>
<div class="hero-line"></div>
<div class="hero-count">01 / 03</div>
<h1 class="hero-title">Dream Home Might Be<br>Much Closer Than You Think</h1>
<div class="btn" style="left:163px;top:438px;width:125px;height:36px">VIEW SERVICES →</div>
<div class="arrow-box" style="left:977px;top:347px;background:var(--gold)"><svg width="16" height="26" viewBox="0 0 16 26"><path d="M2 1l12 12L2 25" fill="none" stroke="#fff" stroke-width="2"/></svg></div>
<div class="arrow-box" style="left:917px;top:407px;background:#1c1c1c"><svg width="16" height="26" viewBox="0 0 16 26"><path d="M14 1L2 13l12 12" fill="none" stroke="#fff" stroke-width="2"/></svg></div>

<section class="welcome">
  <div class="abs" style="left:333px;top:197px;width:234px;height:196px;background:linear-gradient(135deg,#5a3b36,#8a6a55 50%,#3c2a2c)" role="img" aria-label="Cafe interior with arched windows"></div>
  <div class="abs" style="left:162px;top:156px;width:240px;height:202px;border:3px solid #fff;background:linear-gradient(160deg,#6b6b6b,#3a3a3a 60%,#2a2a2a)" role="img" aria-label="Team group photo in studio"></div>
  <svg class="abs" style="left:263px;top:238px" width="38" height="38" viewBox="0 0 38 38"><circle cx="19" cy="19" r="18" fill="#c7a57c" opacity=".9"/><path d="M15 12l10 7-10 7z" fill="#fff"/></svg>

  <div class="abs h2" style="right:163px;top:85px">Welcome To <span class="gold">Our Site</span></div>
  <div class="rule" style="left:987px;top:121px"></div>
  <div class="abs" style="right:163px;top:156px;font-size:14px;font-style:italic">Since we are the best, together we can do miracles!</div>
  <p class="abs para" style="right:163px;top:186px;width:420px;text-align:right">Lorem ipsum dolor amet freegan fashion axe umami, fam ennui hot chicken mixtape tumeric. Plaid PBR&amp;B cardigan sriracha, next level yuccie air plant selfiesasr banh mi for a palosanto. Brooklyn man bun DIY, copper mug wayfarers schlitz hella</p>
  <p class="abs para" style="right:163px;top:260px;width:420px;text-align:right">Portland shabby chic chillwave, narwhal kombucha flannel tilde. Jean shorts after a farm-to-table tbh cray echo park squid everyday carry wayfarers affogato etsymaloi truffauter hexagon kickstarter cornhole</p>
  <div class="btn" style="left:631px;top:356px;width:115px;height:38px">MORE ABOUT US</div>
  <div class="abs" style="left:758px;top:366px;font-size:14px;font-style:italic">Request a quote: <span class="gold" style="font-family:'Playfair Display',serif;font-size:13px">freequote@example.com</span></div>
</section>

<section class="services">
  <div class="abs h2" style="left:162px;top:121px">Our <span class="gold">Services</span></div>
  <div class="rule" style="left:163px;top:156px"></div>
  <p class="abs para" style="left:161px;top:182px;width:210px">Lorem ipsum dolor amet freegan fashion axe umami, fam ennui hot chicken mixtape tumeric. Plaid PBR&amp;B cardigan sriracha, next level yuccie air plant selfiesasr a banh mi for a palosanto.</p>
  <div class="btn" style="left:163px;top:322px;width:101px;height:37px">ALL SERVICES</div>

  <div class="abs" style="left:406px;top:89px;width:210px;height:306px;background:linear-gradient(180deg,#2a2a2a,#1f1f1f);border:1px solid #bbb;text-align:center">
    <svg style="margin-top:90px" width="38" height="36" viewBox="0 0 38 36"><rect x="2" y="6" width="28" height="28" fill="none" stroke="#fff" stroke-width="1.5"/><path d="M8 28L30 6l4 4L12 32z" fill="none" stroke="#fff" stroke-width="1.5"/></svg>
    <div style="font-size:11px;font-weight:600;margin-top:14px">ARCHITECTURE</div>
    <div style="font-size:10px;line-height:22.5px;margin-top:6px;color:#ddd">La croix cardigan 8-bit, celiacefati<br>brunch gochujang tofu fanny</div>
  </div>
  <div class="card-head" style="left:616px;top:89px"><span class="bar"></span><span class="t">INTERIOR DESIGN</span><span class="r">READ MORE</span><span class="n">02</span></div>
  <div class="abs" style="left:616px;top:171px;width:210px;height:224px;background:linear-gradient(180deg,#eceae7,#c9b59b 70%,#8b6c4e)" role="img" aria-label="Bright dining room with round table"></div>
  <div class="card-head" style="left:826px;top:89px;width:211px"><span class="bar"></span><span class="t">PROJECT MANAGMENT</span><span class="r">READ MORE</span><span class="n">03</span></div>
  <div class="abs" style="left:826px;top:171px;width:211px;height:224px;background:linear-gradient(135deg,#9a9a96,#6d6d6a 60%,#b5b3ad)" role="img" aria-label="Drafting triangle on technical plans"></div>

  <svg class="abs" style="left:684px;top:426px" width="14" height="20" viewBox="0 0 14 20"><path d="M12 1L3 10l9 9" fill="none" stroke="#fff" stroke-width="1.5"/></svg>
  <svg class="abs" style="left:726px;top:426px" width="32" height="20" viewBox="0 0 32 20"><path d="M1 10h29M21 1l9 9-9 9" fill="none" stroke="#c7a57c" stroke-width="1.5"/></svg>
</section>

<section class="abs" style="left:0;top:1628px;width:1200px;height:1294px;background:var(--projects)">
  <div class="abs h2" style="left:0;width:1200px;top:83px;text-align:center">Our <span class="gold">Projects</span></div>
  <div class="rule" style="left:571px;top:118px;width:58px"></div>

  <div class="abs" style="left:162px;top:169px;width:500px;height:295px;background:linear-gradient(90deg,#9a958d,#6a645c 50%,#2e2e2e 70%,#555)" role="img" aria-label="Hanging pendant bulb against brick wall"></div>
  <div class="proj-panel" style="left:662px;top:169px;width:376px;height:295px">
    <svg class="abs" style="left:46px;top:44px" width="36" height="36" viewBox="0 0 36 36"><rect x="2" y="4" width="24" height="28" fill="none" stroke="#222" stroke-width="1.5"/><path d="M10 26L30 6l4 4-20 20z" fill="none" stroke="#222" stroke-width="1.5"/></svg>
    <span class="num" style="right:44px;top:40px">01</span>
    <h3 style="left:46px;top:96px">Concept &amp; Details</h3>
    <div class="hr" style="left:46px;top:148px;width:284px"></div>
    <p style="left:46px;top:163px;width:290px">Quinoa fixie cloud bread brunch, meditation slow-carb chillwave franzen thundercats taiyaki adaptogen locavores ugh cronut tilde</p>
    <span class="link" style="left:46px;top:245px">VIEW PROJECT</span>
  </div>

  <div class="proj-panel" style="left:162px;top:510px;width:374px;height:295px">
    <svg class="abs" style="left:44px;top:44px" width="36" height="36" viewBox="0 0 36 36"><rect x="2" y="4" width="24" height="28" fill="none" stroke="#222" stroke-width="1.5"/><path d="M10 26L30 6l4 4-20 20z" fill="none" stroke="#222" stroke-width="1.5"/></svg>
    <span class="num" style="right:42px;top:40px">02</span>
    <h3 style="left:44px;top:96px">Perfection</h3>
    <div class="hr" style="left:44px;top:148px;width:284px"></div>
    <p style="left:44px;top:163px;width:290px">Quinoa fixie cloud bread brunch, meditation slow-carb chillwave franzen thundercats taiyaki adaptogen locavores ugh cronut tilde</p>
    <span class="link gold" style="left:44px;top:245px;text-decoration:underline;font-weight:500">VIEW PROJECT</span>
  </div>
  <div class="abs" style="left:536px;top:510px;width:502px;height:295px;background:linear-gradient(135deg,#3e3a37,#2d2a28 50%,#4a3c36)" role="img" aria-label="Dimly lit hotel bedroom"></div>
  <div class="abs" style="left:551px;top:525px;width:472px;height:265px;border:1px solid #bbb"></div>
  <div class="abs" style="left:551px;top:525px;width:472px;height:265px;border-left:none;border-top:none"></div>
  <div class="abs" style="left:706px;top:656px;font-size:11px;font-weight:700;letter-spacing:3px;text-decoration:underline">PALMCREST HOTEL</div>

  <div class="abs" style="left:162px;top:851px;width:500px;height:295px;background:linear-gradient(120deg,#6b3b2c,#b79d86 45%,#e8e2da 60%,#6c4f3a)" role="img" aria-label="Living room with brick fireplace and leather sofas"></div>
  <div class="proj-panel" style="left:662px;top:851px;width:376px;height:295px">
    <svg class="abs" style="left:46px;top:44px" width="36" height="36" viewBox="0 0 36 36"><rect x="2" y="4" width="24" height="28" fill="none" stroke="#222" stroke-width="1.5"/><path d="M10 26L30 6l4 4-20 20z" fill="none" stroke="#222" stroke-width="1.5"/></svg>
    <span class="num" style="right:44px;top:40px">03</span>
    <h3 style="left:46px;top:96px">Design</h3>
    <div class="hr" style="left:46px;top:148px;width:284px"></div>
    <p style="left:46px;top:163px;width:290px">Quinoa fixie cloud bread brunch, meditation slow-carb chillwave franzen thundercats taiyaki adaptogen locavores ugh cronut tilde</p>
    <span class="link" style="left:46px;top:245px">VIEW PROJECT</span>
  </div>

  <div class="abs" style="left:0;width:1200px;top:1190px;text-align:center;font-size:10px;font-weight:700;text-decoration:underline">VIEW ALL PROJECTS</div>
</section>

<section class="contact">
  <div class="abs h2" style="left:162px;top:237px;line-height:30px">Keep in touch and&nbsp; feel free<br>to schedule a consult</div>
  <div class="rule" style="left:163px;top:334px;width:58px"></div>
  <p class="abs para" style="left:161px;top:345px;width:340px">Lorem ipsum dolor amet freegan fashion axe umami, fam ennui hot chicken mixtape tumeric. Plaid PBR&amp;B cardigan sriracha</p>
  <form class="form">
    <div class="field" style="top:45px">Your Name Here*</div>
    <div class="field" style="top:98px">Your E-mail Here*</div>
    <div class="field" style="top:151px">Subject*</div>
    <div class="field" style="top:204px;height:108px">Type text here...</div>
    <div class="btn" style="left:45px;top:325px;width:412px;height:44px;border-radius:0">SEND MESSAGE</div>
  </form>
</section>

</body>
</html>
```